Alternative Health business needs a self help book cover design

Pale Brook Healing requires an E book and print cover design for a new self help book titled "Making The Bright Choice". Sub title 'Ways to build the glad days YOU seek' . Author Dorinda Crastley. The book is about deliberately changing things now, so you feel happy now and this then flows out an effects everything else in your life. It combines NLP, yoga philosophy and modern psychology in a down to earth, easy to read manner. I would like the cover to be happy, colourful, beautiful, artistic and hip. Maybe something hand drawn or painted. Something a woman would want to display and something that makes you smile and feel happy.
I don't want it to look like a romance novel and would prefer no photos of people. Pics are of other peoples covers I like. Thank you in advance. dorinda

Target Market(s)

woman 18-50

Industry/Entity Type

Business

Requirements
Must have
• happy feeling. professional look
Nice to have
• original drawing or painting
Should not have
• photos of real people, yellow smiley faces, sunsets, butterflies, yoga, tree, elements of my business logo

```html
<!DOCTYPE html>
<html lang="en">
<head>
<meta charset="utf-8">
<title>Making The Bright Choice — Dorinda Crastley</title>
<link rel="stylesheet" href="https://fonts.googleapis.com/css2?family=Arvo:wght@700&family=Rye&family=Reenie+Beanie&display=swap">
<style>
  :root {
    --backdrop: #bcdcd3;
    --paper: #e9e8e5;
    --paper-light: #f4f3f1;
    --paper-shade: #dddbd6;
    --olive: #5a5f45;
    --ink: #2f3227;
    --coral: #e8643a;
    --rose: #d9345a;
    --amber: #f08a2c;
    --teal: #6cc3b8;
    --heart: #e23d3b;
  }
  * { box-sizing: border-box; margin: 0; padding: 0; }
  html, body {
    width: 1200px;
    height: 1200px;
    overflow: hidden;
    background: var(--backdrop);
  }
  .canvas {
    position: relative;
    width: 1200px;
    height: 1200px;
    display: flex;
    align-items: center;
    justify-content: center;
  }
  .book-cover {
    position: relative;
    width: 760px;
    height: 1140px;
    background:
      radial-gradient(ellipse 40% 25% at 20% 30%, var(--paper-light), transparent 70%),
      radial-gradient(ellipse 35% 20% at 80% 65%, var(--paper-light), transparent 70%),
      radial-gradient(ellipse 30% 18% at 30% 85%, var(--paper-shade), transparent 70%),
      radial-gradient(ellipse 30% 15% at 75% 15%, var(--paper-shade), transparent 70%),
      var(--paper);
    display: flex;
    flex-direction: column;
    align-items: center;
  }
  .author-name {
    margin-top: 78px;
    font-family: "Arvo", Georgia, serif;
    font-weight: 700;
    font-size: 34px;
    letter-spacing: 3px;
    text-transform: uppercase;
    color: var(--olive);
  }
  .book-title {
    margin-top: 40px;
    display: flex;
    flex-direction: column;
    align-items: center;
    font-family: "Rye", Georgia, serif;
    font-weight: 400;
    line-height: 1;
    white-space: nowrap;
  }
  .book-title span {
    display: block;
    background: linear-gradient(100deg, var(--rose), var(--coral) 45%, var(--amber) 70%, var(--rose));
    -webkit-background-clip: text;
    background-clip: text;
    color: transparent;
  }
  .title-making { font-size: 84px; letter-spacing: 4px; }
  .title-the {
    font-size: 40px;
    letter-spacing: 8px;
    margin: 14px 0 10px;
  }
  .title-the::before, .title-the::after {
    content: "";
    display: inline-block;
    width: 44px;
    height: 5px;
    margin: 0 14px;
    vertical-align: middle;
    background: var(--coral);
  }
  .title-bright { font-size: 108px; letter-spacing: 2px; }
  .title-choice { font-size: 108px; letter-spacing: 2px; margin-top: 6px; }
  .heart-mark {
    margin-top: 48px;
    width: 46px;
    height: 42px;
  }
  .book-subtitle {
    margin-top: 26px;
    display: flex;
    flex-direction: column;
    align-items: center;
    font-family: "Reenie Beanie", cursive;
    color: var(--olive);
    line-height: 0.95;
    white-space: nowrap;
  }
  .subtitle-lead { font-size: 52px; }
  .subtitle-close { font-size: 76px; }
  .publisher-name {
    position: absolute;
    bottom: 74px;
    left: 0;
    right: 0;
    text-align: center;
    font-family: "Arvo", Georgia, serif;
    font-weight: 700;
    font-size: 20px;
    letter-spacing: 1.5px;
    color: var(--ink);
  }
</style>
</head>
<body>
  <main class="canvas">
    <section class="book-cover">
      <p class="author-name">Dorinda Crastley</p>
      <h1 class="book-title">
        <span class="title-making">MAKING</span>
        <span class="title-the">THE</span>
        <span class="title-bright">BRIGHT</span>
        <span class="title-choice">CHOICE</span>
      </h1>
      <svg class="heart-mark" viewBox="0 0 46 42" aria-hidden="true">
        <path d="M23 40 C8 29 2 21 2 13 C2 6 7 2 13 2 C18 2 21 5 23 9 C25 5 28 2 33 2 C39 2 44 6 44 13 C44 21 38 29 23 40 Z" fill="var(--heart)"/>
      </svg>
      <h2 class="book-subtitle">
        <span class="subtitle-lead">Ways to build the glad days</span>
        <span class="subtitle-close">YOU seek</span>
      </h2>
      <p class="publisher-name">PUBLISHER LOGO</p>
    </section>
  </main>
</body>
</html>
```